" Trabalhamos com serviços de TI, gerenciamento e monitoramento de servidores, estações de trabalho e ativos de rede. Vendemos peças de informática no geral. "

```html
<!DOCTYPE html>
<html lang="pt-BR">
<head>
<meta charset="UTF-8">
<title>Cartão de visita – Nortex Tecnologia</title>
<link href="https://fonts.googleapis.com/css2?family=Quicksand:wght@500;600;700&display=swap" rel="stylesheet">
<style>
  :root {
    --page-bg: #e9e7e8;
    --card-top: #f4eff1;
    --card-bottom: #e6dde1;
    --ink: #5e2535;
    --ink-soft: #7a3e4e;
    --accent: #9b2f45;
    --decor: rgba(120, 36, 56, 0.16);
    --edge: rgba(94, 37, 53, 0.18);
  }
  * { box-sizing: border-box; margin: 0; padding: 0; }
  html, body {
    width: 1200px; height: 1200px; overflow: hidden;
    background: var(--page-bg);
    font-family: "Quicksand", sans-serif;
    color: var(--ink);
  }
  .business-card {
    position: absolute;
    left: 100px; top: 272px;
    width: 1000px; height: 655px;
    border-radius: 28px;
    background: linear-gradient(160deg, var(--card-top), var(--card-bottom));
    border: 2px solid var(--edge);
    box-shadow: 0 24px 60px rgba(60, 20, 30, 0.18);
    overflow: hidden;
  }
  .brand-decoration {
    position: absolute;
    left: -170px; top: 20px;
    width: 600px; height: 600px;
    border-radius: 50%;
    background: radial-gradient(circle at 60% 40%, rgba(155, 47, 69, 0.22), var(--decor) 60%, rgba(120, 36, 56, 0.08));
  }
  .holder {
    position: absolute;
    left: 548px; top: 108px;
  }
  .holder-name {
    font-size: 36px; font-weight: 600; line-height: 1.1;
  }
  .holder-role {
    font-size: 22px; font-weight: 600; color: var(--ink-soft);
  }
  .contact-list {
    position: absolute;
    left: 565px; top: 202px;
    list-style: none;
  }
  .contact-item {
    display: flex; align-items: center;
    font-size: 21px; font-weight: 500; line-height: 27px;
    margin-bottom: 12px;
  }
  .contact-icon {
    flex: none; width: 30px; height: 30px; margin-right: 14px;
  }
  .brand-lockup {
    position: absolute;
    left: 560px; top: 462px;
    display: flex; align-items: center; gap: 22px;
  }
  .brand-dot {
    width: 84px; height: 84px; border-radius: 50%;
    background: var(--ink);
  }
  .brand-text {
    font-weight: 600; color: var(--ink); line-height: 1;
  }
  .brand-name { font-size: 72px; letter-spacing: 2px; }
  .brand-sub { font-size: 16px; letter-spacing: 9px; margin-top: 6px; padding-left: 4px; }
</style>
</head>
<body>
  <article class="business-card">
    <div class="brand-decoration" role="img" aria-label="Elemento decorativo grande e translúcido da marca"></div>

    <header class="holder">
      <h1 class="holder-name">Nome Completo</h1>
      <p class="holder-role">Administrador</p>
    </header>

    <ul class="contact-list">
      <li class="contact-item">
        <svg class="contact-icon" viewBox="0 0 30 30" aria-hidden="true">
          <circle cx="15" cy="15" r="13" fill="none" stroke="var(--ink)" stroke-width="2"/>
          <path d="M10.5 9.5c1-1 2-.6 2.4.2l1 2c.3.6 0 1.2-.5 1.6l-.7.5c.7 1.6 2 2.9 3.5 3.6l.6-.7c.4-.5 1-.7 1.6-.4l2 1c.8.4 1 1.5.2 2.3-1.4 1.4-3.4 1.2-5.5-.2-2.1-1.4-3.8-3.3-4.7-5.4-.7-1.7-.6-3.3.1-4.5z" fill="var(--ink)"/>
        </svg>
        <span>(41) 3000-1234<br>(41) 99000-5678</span>
      </li>
      <li class="contact-item">
        <svg class="contact-icon" viewBox="0 0 30 30" aria-hidden="true">
          <circle cx="15" cy="15" r="13" fill="none" stroke="var(--ink)" stroke-width="2"/>
          <path d="M15 7.5a5 5 0 0 0-5 5c0 3.8 5 9.5 5 9.5s5-5.7 5-9.5a5 5 0 0 0-5-5z" fill="var(--ink)"/>
          <circle cx="15" cy="12.5" r="1.8" fill="var(--card-top)"/>
        </svg>
        <span>Rua das Acácias, 120 sl. 04<br>Centro (Curitiba/PR)<br>CEP: 80000-100</span>
      </li>
      <li class="contact-item">
        <svg class="contact-icon" viewBox="0 0 30 30" aria-hidden="true">
          <circle cx="15" cy="15" r="13" fill="none" stroke="var(--ink)" stroke-width="2"/>
          <circle cx="15" cy="15" r="7" fill="none" stroke="var(--ink)" stroke-width="1.6"/>
          <ellipse cx="15" cy="15" rx="3" ry="7" fill="none" stroke="var(--ink)" stroke-width="1.4"/>
          <line x1="8" y1="15" x2="22" y2="15" stroke="var(--ink)" stroke-width="1.4"/>
        </svg>
        <span>nortexti.com</span>
      </li>
      <li class="contact-item">
        <svg class="contact-icon" viewBox="0 0 30 30" aria-hidden="true">
          <circle cx="15" cy="15" r="13" fill="none" stroke="var(--ink)" stroke-width="2"/>
          <rect x="8.5" y="10" width="13" height="10" rx="1.5" fill="none" stroke="var(--ink)" stroke-width="1.6"/>
          <path d="M8.8 10.8 15 15.5l6.2-4.7" fill="none" stroke="var(--ink)" stroke-width="1.6"/>
        </svg>
        <span>contato@nortexti.com</span>
      </li>
    </ul>

    <div class="brand-lockup">
      <span class="brand-dot" aria-hidden="true"></span>
      <div class="brand-text">
        <div class="brand-name">NORTEX</div>
        <div class="brand-sub">TECNOLOGIA</div>
      </div>
    </div>
  </article>
</body>
</html>
```